Kestrel Dawn Magazine need Logo desing and front page for 1 edittion

This is a new magazine that will be circulating in Panama. the magazine will run non for profit,will be mostly informative and few advertizers to cover printing costs.
the magaine will oncce every 2 or 3 month. we need to present it to the editors who will be aproving or diss aproving the project.

we need a Logo desing for the name of the magazine "Kestrel Dawn" and the "front cover desing for the first edition" it will be good if the designer can incude the designed format for the iner magazine, for us just to add in the artucles and the spaces for advertizing.

the magazine content will be articles by govenment energy sectors, gloval warming articles, articles in renewvable enery, university profesor talking or promoting new ideas or university advances, orientations, special edition on book or international articles about the subject on saving enerty, different sectors, world innovations in renewbable energy, and the companies who will advertize will be comapnies selling VRAX products, companies offfering product and services on renewvable energy, Led product and systems companies etc...

```html
<!DOCTYPE html>
<html lang="en">
<head>
<meta charset="utf-8">
<title>Kestrel Dawn Magazine – Cover Story Spread</title>
<link rel="stylesheet" href="https://fonts.googleapis.com/css2?family=Libre+Bodoni:wght@500;700&family=Jost:ital,wght@0,300;0,400;1,300;1,400&display=swap">
<style>
  :root {
    --paper: #ffffff;
    --ink: #231f20;
    --brand-green: #1f9e3a;
    --headline-red: #c8202f;
    --box-red: #d0262c;
    --photo-light: #e4efe9;
    --photo-mid: #a9cbb6;
    --photo-dark: #6f9d86;
  }
  * { box-sizing: border-box; margin: 0; padding: 0; }
  html, body { width: 1200px; height: 776px; overflow: hidden; background: var(--paper); }
  .spread {
    position: relative; width: 1200px; height: 776px;
    font-family: "Jost", "Futura", sans-serif; color: var(--ink);
  }
  .section-bar {
    position: absolute; left: 25px; top: 28px; width: 547px; height: 22px;
    background: var(--brand-green); color: #fff;
    font-family: "Libre Bodoni", serif; font-size: 16px; line-height: 22px; padding-left: 4px;
  }
  .headline {
    position: absolute; left: 28px; top: 132px; width: 560px;
    font-family: "Libre Bodoni", serif; font-weight: 500; color: var(--headline-red);
    font-size: 49px; line-height: 56px; letter-spacing: -0.3px;
  }
  .column {
    position: absolute; overflow: hidden;
    font-size: 12.4px; line-height: 16.3px; text-align: justify; hyphens: auto;
  }
  .column p { margin: 0; }
  .drop-cap {
    float: left; font-family: "Jost", sans-serif; font-weight: 300;
    font-size: 84px; line-height: 66px; margin: 0 4px -4px -2px;
  }
  .subhead {
    font-family: "Libre Bodoni", serif; font-weight: 500; color: var(--headline-red);
    font-size: 16.5px; line-height: 20px; margin: 6px 0 2px;
  }
  .feature-photo {
    position: absolute; left: 627px; top: 28px; width: 573px; height: 392px;
    background:
      radial-gradient(ellipse at 30% 55%, var(--photo-light) 0%, transparent 60%),
      linear-gradient(160deg, var(--photo-dark) 0%, var(--photo-mid) 45%, var(--photo-light) 100%);
  }
  .pull-message {
    position: absolute; left: 958px; top: 296px; width: 230px;
    font-family: "Jost", sans-serif; font-weight: 300; font-style: italic;
    font-size: 30px; line-height: 33px; color: var(--ink);
  }
  .opinion-box {
    position: absolute; left: 815px; top: 590px; width: 368px; height: 143px;
    background: var(--box-red); color: #fff; border-radius: 10px; padding: 8px 12px;
  }
  .opinion-box h2 {
    font-family: "Libre Bodoni", serif; font-weight: 700; font-size: 18px; line-height: 22px; margin-bottom: 4px;
  }
  .opinion-box p { font-style: italic; font-size: 12px; line-height: 16.5px; }
  .folio {
    position: absolute; top: 744px; font-family: "Libre Bodoni", serif; font-size: 14px; line-height: 16px;
  }
  .masthead-mark {
    position: absolute; top: 744px; font-family: "Jost", sans-serif; font-weight: 400;
    font-size: 14px; line-height: 16px; color: var(--brand-green);
  }
</style>
</head>
<body>
<main class="spread">
  <!-- Left page -->
  <div class="section-bar">Cover Story</div>
  <h1 class="headline">Global warming and<br>the energy management</h1>

  <div class="column" style="left:28px; top:258px; width:170px; height:486px;">
    <p><span class="drop-cap">K</span>o hi, obus sesid confex sena nonstum nonsultorio, taliciam, quium incipesNon tem verissu libusa re muscem iumus, et;To elicaet? Risquam tereis. Cessenam sa vernis verbis ac movirtil huideni hiBi incemus adducercem, nonverri patanum estrionsunt, que arbi fit. Tor untiu voc mius et ventus, ficte, que prox manteret iliamquit; ne forteli, nostraedees intem ce teriusquem et quam iaetri sendiis acrebatuit, quamqua mquitar istraes es Martimulium morturox nos vil hil unum P. meratua mquam, consus ampratil hos ca; ego essesid dem ocussol udeate, modica rehem quam stium porum consus? At abes inam. Dam ut publint imilium hosticam ad mo aris il cae avemod proximora, unum coendam duc res inculvi dicepervir horarte rratem. Grariberum retissus sis. Lost int? Elut nos ne publinc erario.</p>
  </div>

  <div class="column" style="left:216px; top:258px; width:171px; height:486px;">
    <p>ario, pra nondeatus me aur ade morudam opostorum, et gratrum o erem ditatque ia ad meris acii pra, peris; C. Cato et; nitin nia ta inerfer vivirma, consuppl. Erimmorei publici diciendum oruntem nes potis culutus iptiam vis, utus for adela manum adhum iam nostreb efaceris, ut verfex nos viconum nonsulegili iaequam crissus ceme di pris. Robut acchuid erfirib utebatiam sens se, trarter estrice rissolicae qua tabem, consupp lissidi pra vestracta vastis. Valabulvili, Cat.</p>
    <h2 class="subhead">The problem</h2>
    <p>Si iaequa reviliculus cris. Ad mum cae clego avo, morte, Paliamed con andientiliam usquonf ecurorae ne confina tustre, te non hos in peris dem dum tuam nicultus, cae nosta vividelatum con vero im noximussa rescrum porum consusq uamendit quod nostemus. Aximus liissi fachucta,</p>
  </div>

  <div class="column" style="left:404px; top:258px; width:169px; height:486px;">
    <p>senimortiam tes vivatus vis ego condie prorae eo, nonlocur hae cae cre, menducipte pritimus ma, stis.</p>
    <p>Ximedii considiu consiss umumus, Castide liconsula duconihicam hus</p>
    <h2 class="subhead">The solutions</h2>
    <p>publiae convere contere ssedo, cone alestia noca aderobus in ac mo aude ad co ut finam publis. Do, quit? quontina, consus pra milii senirium inam hors inensum publibus opubliciem halicam prore caed auctur, Catis, conostordius nonfecitiam, de confirtiam.</p>
    <p>Rae inatebatum lostem aut factum ori se fex moltum nostimus ilibus henatus iam ego publicae iam perce eorteris. Graet ia deffrem arei fur hillari pionsup ientebus bonum, tississulius occhuit actum rehena, sullerid ius, crendam macii etodit pratimurs M. Vala pos ne mena, quo</p>
  </div>

  <div class="folio" style="left:28px;">4</div>
  <div class="masthead-mark" style="left:478px;">Kestrel Dawn</div>

  <!-- Right page -->
  <div class="feature-photo" role="img" aria-label="Photo: a hand placing a glass cube into a wall of cubes showing green energy icons, over a puzzle world map"></div>
  <p class="pull-message">Your important message lines go over here…</p>

  <div class="column" style="left:627px; top:428px; width:171px; height:316px;">
    <p>nostis; nocrum untem haberius, potiquem obse consus culiquium, nori teri publiqu idepse nequam anum Romnonsua di iaesil hos ina, nors nente fescit ac tesse consultorem Palice et ips, te, Catum oritiss ulesta, vertatus, publius, perrae perae de quit, nem perore in Etra nonstil ubliciam in tam tes condam re atu elicit cotalatum diem venatario publis cupio, efacrum urnimilis, Cati, prest? quem hoste cenatum aut ad nim cuppl. Senem porbem re publint iliciam poentum ponim movervi dernitus omanum re, niam es?</p>
  </div>

  <div class="column" style="left:815px; top:428px; width:170px; height:150px;">
    <p>Ebus criam cotemGit, unulvid publis, in se diestiam mod in ta opostio rbitum mora rei sentem hor quemus viri ius. Iquo efacto vivero pesto viviris mactum is ad firmactus re, P. Epoerissedo, culis cus, senat quem consilina, peces perfessimis. Ahacrei fac tes</p>
  </div>

  <div class="column" style="left:1003px; top:428px; width:172px; height:150px;">
    <p>viverions essiliusqua consunt eludem nDetodisque ad in senihilis. Xima, qui premuraetis, qua nos veris? Git. Ederum interes ommo auEhenima inctotae. Upid quatMorum Romprav eritatum rem niam dierviriorio adem in patum tem, est pra et pu</p>
  </div>

  <aside class="opinion-box">
    <h2>Your opinion is very important to us</h2>
    <p>ZDe es, fordiem overic tus, que aperess erimus iam nonsula vit, con aceste nes, quo C. Go me cum incepon iuspio et, inatum inatilles vius nortum ad des habem se desimpostem untrudemus se confecto egerorumurs praternin sedo, oc te pat, quastis Catus constemus confeci buncero­riam. Fintratu qui inihilia? As catior pris faccii conine.</p>
  </aside>

  <div class="masthead-mark" style="left:629px;">Kestrel Dawn</div>
  <div class="folio" style="left:1164px;">5</div>
</main>
</body>
</html>
```